An international wholesale business needs letterhead design

Logo file is attached. Please design a letterhead with the following details:

- Company Name and Logo
- Address
- VAT Registration number
- Phone No
- Website address

```html
<!DOCTYPE html>
<html lang="en">
<head>
<meta charset="UTF-8">
<title>Corvane Trading — Letterhead</title>
<link href="https://fonts.googleapis.com/css2?family=Montserrat:wght@400;500;600&display=swap" rel="stylesheet">
<style>
  :root {
    --backdrop: #e4e4e4;
    --paper: #ffffff;
    --brand-red: #c5222c;
    --brand-grey: #8e979e;
    --ink: #3a3a3a;
    --rule: #9a9a9a;
  }
  * { box-sizing: border-box; margin: 0; padding: 0; }
  html, body {
    width: 1200px;
    height: 874px;
    overflow: hidden;
    background: var(--backdrop);
    font-family: "Montserrat", Arial, sans-serif;
  }
  .letterhead {
    position: absolute;
    left: 317px;
    top: 37px;
    width: 566px;
    height: 800px;
    background: var(--paper);
    box-shadow: 0 4px 18px rgba(0,0,0,0.12);
  }
  .brand {
    position: absolute;
    left: 40px;
    top: 46px;
    display: flex;
    align-items: center;
    gap: 10px;
  }
  .brand-mark {
    width: 30px;
    height: 30px;
    border: 3px solid var(--brand-red);
    border-radius: 50%;
  }
  .brand-name {
    font-size: 22px;
    font-weight: 600;
    letter-spacing: 1px;
    color: var(--brand-red);
    text-transform: uppercase;
    white-space: nowrap;
  }
  .contact {
    position: absolute;
    right: 40px;
    top: 40px;
    padding-left: 10px;
    border-left: 1px solid var(--rule);
    font-size: 8.5px;
    line-height: 1.55;
    color: var(--ink);
    list-style: none;
    white-space: nowrap;
  }
  .contact li { display: flex; align-items: center; gap: 4px; }
  .contact svg { width: 7px; height: 7px; fill: var(--brand-red); flex: none; }
  .footer-bands {
    position: absolute;
    left: 0;
    bottom: 0;
    width: 566px;
    height: 12px;
  }
</style>
</head>
<body>
  <main class="letterhead">
    <header class="brand">
      <span class="brand-mark"></span>
      <span class="brand-name">Corvane Trading</span>
    </header>

    <ul class="contact">
      <li>118 Harbour Lane Name</li>
      <li>Country Name QX 40218</li>
      <li><svg viewBox="0 0 10 10"><path d="M2 0.5 L4 2.6 L3 3.8 Q4.3 6 6.2 7 L7.4 6 L9.5 8 L8.2 9.5 Q3.5 9 0.5 1.8 Z"/></svg>(555) 218-4630</li>
      <li><svg viewBox="0 0 10 10"><rect x="0.5" y="2" width="9" height="6.5" rx="0.8"/><path d="M1 2.5 L5 5.8 L9 2.5" stroke="#fff" stroke-width="0.9" fill="none"/></svg>info@corvanetrading.com.au</li>
      <li><svg viewBox="0 0 10 10"><circle cx="5" cy="5" r="4.5"/><path d="M0.5 5 H9.5 M5 0.5 Q2.3 5 5 9.5 M5 0.5 Q7.7 5 5 9.5" stroke="#fff" stroke-width="0.7" fill="none"/></svg>www.corvanetrading.com.au</li>
      <li>VAT Registration No : 604317</li>
    </ul>

    <svg class="footer-bands" viewBox="0 0 566 12" preserveAspectRatio="none" aria-hidden="true">
      <polygon points="0,5 346,5 340,12 0,12" fill="var(--brand-red)"/>
      <polygon points="352,0 566,0 566,12 343,12" fill="var(--brand-grey)"/>
    </svg>
  </main>
</body>
</html>
```